Brinevale Yacht Management Full Page Ad Flyer

Yacht Management Package also includes the following periodic Monthly services:

Monthly full vessel systems checklist inspections
Diver For Hull Cleaning And Inspection Of Props, Shafts, and Zincs
Interior/Exterior Detailing and scheduled washdowns
Manage Haulout
Pump-out Services
On-call Captain and Crew Services
Updates

Need more time to provide more content to designers and the printing press template file.

Target Market(s)

Vessel owners, motor yachts, sailboats from 25 feet in length up to 125 feet in length. We do not do cruise ships or yachts larger than 125 feet. Someone who has their boat docked at their house or a local marina. We also offer mobile on-site services.

```html
<!DOCTYPE html>
<html lang="en">
<head>
<meta charset="utf-8">
<title>Brinevale Yacht Management – Nautical Services</title>
<link rel="stylesheet" href="https://fonts.googleapis.com/css2?family=Montserrat:wght@300;400;700&display=swap">
<style>
  :root{
    --navy:#121a3a;
    --navy-panel:#1b2348;
    --gold:#a88a55;
    --gold-text:#c9a15c;
    --white:#ffffff;
    --brand-blue:#1d4f9e;
    --sky-top:#5f95c9;
    --sky-mid:#cfe0ef;
    --water:#3f6f8f;
  }
  *{margin:0;padding:0;box-sizing:border-box}
  html,body{width:675px;height:1200px;overflow:hidden;background:var(--white)}
  body{font-family:"Montserrat",sans-serif;color:var(--white)}
  .flyer{position:relative;width:675px;height:1200px;overflow:hidden;background:var(--white)}
  .backdrop{position:absolute;inset:0}
  .service-list{position:absolute;list-style:none}
  .service-list li{position:relative;font-size:18.5px;line-height:22px;font-weight:400;padding-left:18px}
  .service-list li::before{content:"";position:absolute;left:-0px;top:8px;width:6px;height:6px;background:var(--white)}
  .monthly-list{left:482px;top:594px;width:190px}
  .monthly-list li{margin-bottom:22px}
  .monthly-list li:nth-child(3){margin-bottom:33px}
  .monthly-list li:nth-child(4){margin-bottom:22px}
  .core-list{left:248px;top:919px;width:200px}
  .core-list li{margin-bottom:22px}
  .services-title{position:absolute;left:257px;top:842px;font-size:22.5px;line-height:28px;font-weight:700;color:var(--gold-text)}
  .brand{position:absolute;left:-100px;top:825px;width:456px;height:80px;transform:rotate(-90deg);transform-origin:center}
  .brand-name{display:block;font-size:58px;line-height:62px;font-weight:300;letter-spacing:6px;color:var(--brand-blue);text-align:center}
  .brand-tagline{display:block;font-size:13px;line-height:16px;font-weight:300;letter-spacing:9.5px;color:#555b6e;text-align:center;margin-top:2px}
  .footer-phone{position:absolute;left:0;top:1138px;width:226px;height:62px;background:var(--navy);display:flex;align-items:center;justify-content:center;font-size:17.5px;font-weight:700}
  .footer-tagline{position:absolute;left:226px;top:1138px;width:449px;height:62px;background:var(--gold);display:flex;align-items:center;justify-content:center;font-size:17.5px;font-weight:700}
</style>
</head>
<body>
<main class="flyer">
  <svg class="backdrop" width="675" height="1200" viewBox="0 0 675 1200" aria-hidden="false">
    <defs>
      <linearGradient id="skyLeft" x1="0" y1="0" x2="0" y2="1">
        <stop offset="0" stop-color="var(--sky-top)"/>
        <stop offset="0.45" stop-color="var(--sky-mid)"/>
        <stop offset="0.7" stop-color="#c9cfd6"/>
        <stop offset="1" stop-color="#3d5f6e"/>
      </linearGradient>
      <linearGradient id="skyMiddle" x1="0" y1="0" x2="0" y2="1">
        <stop offset="0" stop-color="#9fc0dc"/>
        <stop offset="0.35" stop-color="#e6eef5"/>
        <stop offset="0.62" stop-color="#dfe5ea"/>
        <stop offset="0.72" stop-color="#4a6c86"/>
        <stop offset="1" stop-color="var(--water)"/>
      </linearGradient>
      <linearGradient id="skyRight" x1="0" y1="0" x2="0" y2="1">
        <stop offset="0" stop-color="#8fb5d6"/>
        <stop offset="0.5" stop-color="#e9edf1"/>
        <stop offset="1" stop-color="#b9c3cc"/>
      </linearGradient>
    </defs>

    <!-- left column -->
    <polygon points="0,0 225,0 225,194 0,78" fill="var(--navy)"/>
    <polygon role="img" aria-label="Photo of a white motor yacht moored at a wooden dock under a blue sky" points="0,88 225,200 225,594 0,481" fill="url(#skyLeft)"/>
    <line x1="0" y1="80" x2="225" y2="196" stroke="var(--gold)" stroke-width="4"/>
    <line x1="0" y1="122" x2="225" y2="232" stroke="var(--gold)" stroke-width="1.5" opacity="0.6"/>
    <line x1="0" y1="486" x2="225" y2="600" stroke="var(--gold)" stroke-width="4"/>

    <!-- middle column -->
    <polygon role="img" aria-label="Photo of a sailboat mast and hull over calm marina water" points="226,0 450,0 450,706 226,819" fill="url(#skyMiddle)"/>
    <polygon points="226,831 338,778 450,831 450,1138 226,1138" fill="var(--navy-panel)"/>
    <line x1="369" y1="780" x2="450" y2="739" stroke="var(--gold)" stroke-width="5"/>
    <line x1="392" y1="792" x2="450" y2="762" stroke="var(--gold)" stroke-width="3"/>

    <!-- right column -->
    <polygon role="img" aria-label="Photo of a large white luxury motor yacht with radar mast" points="451,206 675,94 675,481 451,600" fill="url(#skyRight)"/>
    <line x1="451" y1="194" x2="675" y2="78" stroke="var(--gold)" stroke-width="5"/>
    <line x1="451" y1="232" x2="675" y2="120" stroke="var(--gold)" stroke-width="3"/>
    <polygon points="451,600 675,481 675,1138 451,1138" fill="var(--navy)"/>
    <line x1="451" y1="596" x2="675" y2="478" stroke="var(--gold)" stroke-width="5"/>
  </svg>

  <div class="brand">
    <span class="brand-name">BRINEVALE</span>
    <span class="brand-tagline">YACHT MANAGEMENT</span>
  </div>

  <h2 class="services-title">NAUTICAL<br>SERVICES</h2>
  <ul class="service-list core-list">
    <li>Motor Yachts &amp; Sailboats (25-125 Feet)</li>
    <li>Docked at Home or Local Marinas</li>
    <li>Mobile On-Site Service Available</li>
  </ul>

  <ul class="service-list monthly-list">
    <li>Monthly full vessel systems checklist inspections</li>
    <li>Diver For Hull Cleaning And Inspection Of Props, Shafts, and Zincs</li>
    <li>Interior / Exterior Detailing and scheduled washdowns</li>
    <li>Manage Haulout</li>
    <li>Pump-out Services</li>
    <li>On-call Captain and Crew Services</li>
  </ul>

  <div class="footer-phone">+91 8000 4127</div>
  <div class="footer-tagline">Convenient, Tailored Yacht Care</div>
</main>
</body>
</html>
```